Tavo Payments Business card refresh

Need a new design of our business card The info is not what is on these cards i sent this for a reference. I can email all the info over
Info would be Derek Whitfield Chief TAVO is the title. our new address is 47615 Birch Hollow Rd. Oakmere Vale Ca 91384 Cell number is 805-634-2917 Work number is 855-482-7309 ext 212 Derek@tavopayments.com is my email address
Target Market(s)
Merchant Services all businesses that take credit cards
Industry/Entity Type
Merchant Services / Credit Card processing
Contact Information for Business Card
Need a new design of our business card The info is not what is on these cards i sent this for a reference. I can email all the info over Info would be Derek Whitfield Chief TAVO is the title. our new address is 47615 Birch Hollow Rd. Oakmere Vale Ca 91384 Cell number is 805-634-2917 Work number is 855-482-7309 ext 212 Derek@tavopayments.com is my email address
Requirements
Must have
- My logo and colors from my brand guidelines
Nice to have
- i sent some designs just need a new refresh
Should not have
- nothing specific

```html
<!DOCTYPE html>
<html lang="en">
<head>
<meta charset="utf-8">
<title>Tavo Payments Business Card</title>
<link rel="stylesheet" href="https://fonts.googleapis.com/css2?family=Lato:wght@400;700&display=swap">
<style>
  :root {
    --backdrop: #2f3235;
    --brand-green: #a2be2e;
    --ink-dark: #303336;
    --ink-grey: #58595b;
    --paper: #ffffff;
  }
  html, body {
    margin: 0;
    padding: 0;
    width: 1200px;
    height: 1200px;
    overflow: hidden;
    background: var(--backdrop);
    font-family: "Lato", Arial, sans-serif;
  }
  .canvas {
    position: relative;
    width: 1200px;
    height: 1200px;
  }
  .card {
    position: absolute;
    left: 252px;
    width: 699px;
    height: 402px;
    background: var(--paper);
    box-shadow: 0 14px 18px rgba(0,0,0,0.35);
    overflow: hidden;
  }
  .card svg { display: block; width: 100%; height: 100%; }
  .card--front { top: 106px; }
  .card--back { top: 600px; }
  .wordmark { font-family: "Lato", Arial, sans-serif; font-weight: 700; }
  .text-body { font-family: "Lato", Arial, sans-serif; }
</style>
</head>
<body>
<main class="canvas">

  <section class="card card--front" aria-label="Card front">
    <svg viewBox="0 0 1126 648" xmlns="http://www.w3.org/2000/svg">
      <path class="front-field" fill="var(--brand-green)"
        d="M228 0 L1126 0 L1126 90 C1126 350 1050 560 900 648 L0 648 L0 570 C0 300 100 90 228 0 Z"/>
      <path class="swoosh" fill="none" stroke="var(--paper)" stroke-width="7" stroke-linecap="round"
        d="M166 72 C60 200 4 380 2 560"/>
      <path class="swoosh" fill="none" stroke="var(--paper)" stroke-width="7" stroke-linecap="round"
        d="M960 578 C1060 460 1120 300 1124 100"/>
      <text class="wordmark" x="575" y="342" text-anchor="middle" font-size="168" fill="var(--paper)" letter-spacing="4">TAVO</text>
      <text class="wordmark" x="581" y="408" text-anchor="middle" font-size="44" fill="var(--paper)" letter-spacing="31">PAYMENTS</text>
      <text class="text-body" x="563" y="620" text-anchor="middle" font-size="30" fill="var(--paper)">www.tavopayments.com</text>
    </svg>
  </section>

  <section class="card card--back" aria-label="Card back">
    <svg viewBox="0 0 1126 650" xmlns="http://www.w3.org/2000/svg">
      <path class="back-field" fill="var(--brand-green)"
        d="M160 650 C560 640 1000 520 1126 268 L1126 650 Z"/>
      <path class="swoosh" fill="none" stroke="var(--brand-green)" stroke-width="12" stroke-linecap="round"
        d="M1005 370 C800 540 450 640 160 650"/>
      <path fill="var(--paper)" d="M160 650 C470 636 820 560 1000 372 C820 548 470 642 160 650 Z"/>

      <text class="wordmark" x="270" y="364" text-anchor="middle" font-size="120" fill="var(--ink-dark)" letter-spacing="3">TAVO</text>
      <text class="wordmark" x="275" y="412" text-anchor="middle" font-size="32" fill="var(--brand-green)" letter-spacing="23">PAYMENTS</text>

      <line class="divider" x1="530" y1="152" x2="530" y2="462" stroke="var(--brand-green)" stroke-width="3"/>

      <text class="text-body" x="804" y="170" text-anchor="middle" font-size="40" font-weight="700" fill="var(--ink-grey)">DEREK WHITFIELD</text>
      <text class="text-body" x="802" y="216" text-anchor="middle" font-size="34" fill="var(--ink-grey)">CHIEF TAVO</text>

      <g class="icon-pin" fill="var(--brand-green)">
        <path d="M597 284 C588 284 582 291 582 299 C582 308 597 320 597 320 C597 320 612 308 612 299 C612 291 606 284 597 284 Z"/>
        <circle cx="597" cy="299" r="5" fill="var(--paper)"/>
      </g>
      <text class="text-body" x="629" y="308" font-size="21" fill="var(--ink-grey)">47615 Birch Hollow Rd. Oakmere Vale Ca 91384</text>

      <g class="icon-mail">
        <rect x="581" y="353" width="33" height="23" fill="var(--brand-green)"/>
        <path d="M581 355 L597.5 368 L614 355" fill="none" stroke="var(--paper)" stroke-width="2.5"/>
      </g>
      <text class="text-body" x="629" y="372" font-size="21" fill="var(--ink-grey)">Derek@tavopayments.com</text>

      <path class="icon-phone" fill="var(--brand-green)"
        d="M588 418 L594 414 L600 424 L596 428 C598 434 602 438 607 441 L611 437 L619 444 L614 450 C600 448 588 432 588 418 Z"/>
      <text class="text-body" x="629" y="427" font-size="21" fill="var(--ink-grey)">555-634-2917</text>
      <text class="text-body" x="629" y="450" font-size="21" fill="var(--ink-grey)">555-482-7309</text>
    </svg>
  </section>

</main>
</body>
</html>
```